Redesign of QuillLexicon.com in Bootstrap 4

Current design of QuillLexicon.com is not responsive. We need to change it to latest version of Bootstrap 4 keeping essential elements in place.

Apart from home page, we need designs for http://www.quilllexicon.com/meaning/cat also.

Coding

Coded - Design and coding required

Number of Pages Required

2 page

Colors
34a7d8

Requirements
Must have
• Bootstrap 4

```html
<!DOCTYPE html>
<html lang="en">
<head>
<meta charset="utf-8">
<title>Quill Lexicon – English Dictionary</title>
<link href="https://fonts.googleapis.com/css2?family=Open+Sans:wght@400;600&family=Ubuntu:wght@300;400;500;700&display=swap" rel="stylesheet">
<style>
:root{
  --orange:#f6a01a;
  --blue-title:#1d5a98;
  --ink:#444;
  --muted:#777;
  --navy:#1a3d6e;
  --gray-bg:#f3f3f3;
  --line:#e2e2e2;
  --footer:#232323;
  --footer-bottom:#1a1a1a;
  --hero-a:#122a44;
  --hero-b:#1e3a57;
  --hero-c:#3d4048;
}
*{margin:0;padding:0;box-sizing:border-box}
html,body{width:746px;height:1200px;overflow:hidden;background:#fff}
body{font-family:"Open Sans",Arial,sans-serif;color:var(--ink);font-size:8px}
.page{position:relative;width:746px;height:1200px;overflow:hidden;border-top:2px solid var(--orange)}
.abs{position:absolute}
.heading{font-family:"Ubuntu",Arial,sans-serif;font-weight:400}

/* header */
.brand{left:62px;top:16px;color:var(--navy);font-family:"Ubuntu",sans-serif;font-weight:700;line-height:1}
.brand .word{display:block;font-size:24px;letter-spacing:.5px}
.brand .sub{display:block;font-size:9px;letter-spacing:1.2px;margin-top:2px}
.account-links{right:62px;top:19px;font-size:7.5px}
.account-links .forgot{color:var(--orange);text-decoration:underline;margin-right:6px}
.account-links .join{color:var(--navy)}
.field{height:21px;border:1px solid #ddd;background:#fff;color:#999;font-size:7px;padding:6px 8px;white-space:nowrap;overflow:hidden}
.btn-orange{background:var(--orange);color:#fff;text-align:center;border-radius:2px;white-space:nowrap}
.login{left:617px;top:37px;width:67px;height:21px;font-size:9px;line-height:21px}

/* nav */
.main-nav{left:61px;top:79px;width:623px;height:31px;display:flex;background:linear-gradient(#f8ac2c,#ee9407);border-radius:2px 2px 0 0;z-index:3}
.main-nav a{color:#fff;font-size:9px;line-height:31px;text-align:center;border-right:1px solid rgba(255,255,255,.25);text-decoration:none}
.main-nav a.active{background:linear-gradient(#3a3a3a,#1d1d1d)}

/* hero */
.hero{left:0;top:93px;width:746px;height:322px}
.hero-scene{left:0;top:0;width:746px;height:322px;background:linear-gradient(180deg,var(--hero-a) 0%,var(--hero-b) 45%,var(--hero-c) 100%)}
.hero-title{left:0;top:98px;width:746px;text-align:center;color:#fff;font-size:21px;font-weight:400}
.hero-search{left:206px;top:140px;width:334px;height:31px;border:1px solid rgba(255,255,255,.7);padding:3px;display:flex;gap:3px}
.hero-search .field{flex:0 0 231px;height:23px;padding:7px 9px}
.hero-search .btn-orange{flex:1;line-height:23px;font-size:9px;border-radius:0}
.arrow{top:142px}

/* features */
.feature-photo{left:61px;top:443px;width:201px;height:133px;border:1px solid #ccc;padding:3px;background:#fff;box-shadow:0 1px 2px rgba(0,0,0,.15)}
.feature-photo div{width:100%;height:100%;background:linear-gradient(135deg,#e9e9e9,#c9c0b8 55%,#e9e9e9)}
.feature-title{left:277px;top:445px;font-size:19px;color:var(--orange);font-weight:400;white-space:nowrap}
.feature-list{left:278px;top:477px;list-style:none}
.feature-list li{height:18.6px;display:flex;align-items:center;gap:7px;font-size:7.5px;white-space:nowrap}
.puzzle{left:552px;top:430px;width:132px;height:147px;border:1px solid var(--line);background:#fff}
.puzzle-head{height:28px;background:var(--orange);color:#fff;font-size:7.5px;line-height:28px;padding-left:7px;position:relative;white-space:nowrap}
.puzzle-head .badge{position:absolute;right:7px;top:5px;width:17px;height:17px;background:#fff}
.puzzle-grid{position:absolute;left:24px;top:32px;width:77px;height:66px;background:#1a3f7f}
.puzzle-note{position:absolute;top:101px;width:100%;text-align:center;font-size:7px;color:var(--muted)}
.puzzle-start{position:absolute;left:20px;top:113px;width:93px;height:23px;line-height:23px;font-size:9px}

/* word of the day */
.wotd{left:0;top:590px;width:746px;height:446px;background:var(--gray-bg);border-top:1px solid var(--line)}
.wotd-title{left:0;top:30px;width:746px;text-align:center;color:var(--orange);font-size:19px}
.card{background:#fff;border:1px solid #e6e6e6;width:302px;height:149px}
.card-title{position:absolute;left:15px;top:13px;font-size:14px;color:var(--blue-title);white-space:nowrap}
.card-photo{position:absolute;width:116px;height:96px;border:1px solid #ccc;padding:2px;background:#fff}
.card-photo div{width:100%;height:100%}
.card-kicker{position:absolute;color:var(--orange);font-size:7.5px}
.card-text{position:absolute;font-size:7.2px;line-height:13.8px;color:#555}
.read-more{position:absolute;width:62px;height:20px;line-height:20px;font-size:7px}
.tidbit{position:absolute;left:12px;top:34px;width:280px;font-size:7.3px;line-height:14px;color:#555}
.tidbit .kw{color:var(--blue-title)}
.tidbit .pos{color:var(--orange);display:block}

/* alphabet */
.browse{left:60px;top:997px;width:96px;height:19px;line-height:19px;font-size:7px;border-radius:2px}
.letters{left:161px;top:997px;display:flex;gap:5px}
.letters span,.next{width:18px;height:19px;line-height:19px;text-align:center;background:linear-gradient(#fafafa,#e1e1e1);border:1px solid #ccc;border-radius:2px;font-size:7px;color:#555}
.next{left:649px;top:997px;width:36px}

/* footer */
.footer{left:0;top:1036px;width:746px;height:130px;background:var(--footer);color:#fff}
.footer .brand{left:60px;top:40px;color:#fff}
.f-col{position:absolute;top:30px}
.f-col h4{font-family:"Ubuntu",sans-serif;font-weight:400;font-size:10.5px;margin-bottom:8px}
.f-col li{list-style:none;font-size:7.5px;height:17px;white-space:nowrap}
.f-col li::before{content:"›";margin-right:10px}
.f-news p{font-size:7.5px;margin-bottom:6px}
.f-news .field{width:144px;height:21px;font-size:7px}
.f-news .btn-orange{width:57px;height:21px;line-height:21px;font-size:7px;margin-top:6px}
.bottom{left:0;top:1166px;width:746px;height:34px;background:var(--footer-bottom);color:#ddd;font-size:7.5px}
.social{position:absolute;top:6px;width:20px;height:20px;border-radius:50%;border:1.5px solid #fff}
</style>
</head>
<body>
<div class="page">

  <header>
    <div class="abs brand"><span class="word">Quill</span><span class="sub">LEXICON</span></div>
    <div class="abs account-links"><span class="forgot">Forgot Password?</span><span class="join">Join for FREE!</span></div>
    <div class="abs field" style="left:365px;top:37px;width:121px">Username...</div>
    <div class="abs field" style="left:492px;top:37px;width:121px">Password...</div>
    <div class="abs btn-orange login">Login</div>
  </header>

  <nav class="abs main-nav">
    <a class="active" style="width:93px">Home</a>
    <a style="width:106px">Idioms</a>
    <a style="width:122px">Common Errors</a>
    <a style="width:116px">Crossword</a>
    <a style="width:80px">Blog</a>
    <a style="width:106px;border:0">Contact</a>
  </nav>

  <section class="abs hero">
    <div class="abs hero-scene" role="img" aria-label="Hero photo: open book and globe in a starry night sky"></div>
    <h1 class="abs heading hero-title">Quill English Dictionary</h1>
    <div class="abs hero-search">
      <div class="field">Enter a word or phrase...</div>
      <div class="btn-orange">Search</div>
    </div>
    <svg class="abs arrow" style="left:31px" width="12" height="34" viewBox="0 0 12 34"><path d="M11 1 1 17l10 16" fill="none" stroke="#fff" stroke-width="1.2"/></svg>
    <svg class="abs arrow" style="left:707px" width="12" height="34" viewBox="0 0 12 34"><path d="M1 1l10 16L1 33" fill="none" stroke="#fff" stroke-width="1.2"/></svg>
  </section>

  <section>
    <div class="abs feature-photo"><div role="img" aria-label="Dictionary with stacked books and a globe"></div></div>
    <h2 class="abs heading feature-title">Search, Save and Master Words</h2>
    <ul class="abs feature-list">
      <li><svg width="9" height="8" viewBox="0 0 9 8"><path d="M1 4l2.5 2.5L8 1" fill="none" stroke="#f6a01a" stroke-width="2"/></svg>Search from more than 300,000 words and phrases</li>
      <li><svg width="9" height="8" viewBox="0 0 9 8"><path d="M1 4l2.5 2.5L8 1" fill="none" stroke="#f6a01a" stroke-width="2"/></svg>Multiple usages to clarify the context</li>
      <li><svg width="9" height="8" viewBox="0 0 9 8"><path d="M1 4l2.5 2.5L8 1" fill="none" stroke="#f6a01a" stroke-width="2"/></svg>Audio, phonetics, meanings, synonyms and antonyms</li>
      <li><svg width="9" height="8" viewBox="0 0 9 8"><path d="M1 4l2.5 2.5L8 1" fill="none" stroke="#f6a01a" stroke-width="2"/></svg>Save the words to your personal deck and access from anywhere</li>
      <li><svg width="9" height="8" viewBox="0 0 9 8"><path d="M1 4l2.5 2.5L8 1" fill="none" stroke="#f6a01a" stroke-width="2"/></svg>It's FREE</li>
    </ul>
    <aside class="abs puzzle">
      <div class="puzzle-head">Today's Crossword Puzzle<span class="badge"></span></div>
      <div class="puzzle-grid" role="img" aria-label="Crossword puzzle grid"></div>
      <div class="puzzle-note">Welcome, Anonymous!</div>
      <div class="btn-orange puzzle-start">Start now</div>
    </aside>
  </section>

  <section class="abs wotd">
    <h2 class="abs heading wotd-title">Word of the Day</h2>

    <article class="abs card" style="left:61px;top:71px">
      <h3 class="heading card-title">English Tidbit</h3>
      <div class="tidbit">
        <span class="pos" style="margin-left:3px">gaffe/gaff</span>
        "Gaffe" is a social blunder and "gaff" is a large hook. Be warned not to make the gaffe of mixing it up with gaff.<br>
        <span class="kw">Gaffe</span> - an unintentional act or remark causing embarrassment to its originator; a blunder.<br>
        <span class="kw">Gaff</span> -&nbsp; 1.a stick with a hook or barbed spear, for landing large fish.<br>
        <span style="padding-left:25px">2.a spar to which the head of a fore-and-aft sail is bent.</span>
      </div>
    </article>

    <article class="abs card" style="left:382px;top:71px">
      <h3 class="heading card-title" style="left:12px">Daily Crossword</h3>
      <div class="card-photo" style="left:12px;top:35px"><div role="img" aria-label="Pen resting on a filled crossword" style="background:linear-gradient(135deg,#d8d8d8,#8a8a8a 55%,#c9b06a)"></div></div>
      <span class="card-kicker" style="left:139px;top:37px">Crossword Lovers!</span>
      <p class="card-text" style="left:139px;top:50px;width:155px">Take this daily crossword challenge from Quill Lexicon.The Crossword Solver found answers to the Lovers crossword clue. The Crossword Solver will often find clues</p>
      <div class="btn-orange read-more" style="left:138px;top:108px">Read more</div>
    </article>

    <article class="abs card" style="left:61px;top:240px">
      <h3 class="heading card-title" style="left:14px">Emberfox Addon</h3>
      <div class="card-photo" style="left:14px;top:35px"><div role="img" aria-label="Phone on a laptop keyboard" style="background:linear-gradient(135deg,#c9c9c9,#6a6a6a 50%,#9a7a55)"></div></div>
      <span class="card-kicker" style="left:141px;top:37px">Crossword Lovers!</span>
      <p class="card-text" style="left:141px;top:50px;width:150px">Add this tool to your Emberfox and quickly look up for definitions from any website without leaving the page. Add this tool to your Emberfox and quickly look</p>
      <div class="btn-orange read-more" style="left:139px;top:108px">Read more</div>
    </article>

    <article class="abs card" style="left:382px;top:240px">
      <h3 class="heading card-title" style="left:13px">Designed for Lumaphone</h3>
      <div class="card-photo" style="left:12px;top:35px"><div role="img" aria-label="Smartphone showing the dictionary app" style="background:linear-gradient(135deg,#e6e6e6,#9a9a9a 50%,#e6e6e6)"></div></div>
      <span class="card-kicker" style="left:140px;top:37px">Crossword Lovers!</span>
      <p class="card-text" style="left:140px;top:50px;width:155px">Quill Lexicon is specially designed for your Lumaphone to quickly lookup meaining, usages and audio of words.Quill Lexicon is specially designed for your Lumaphone</p>
      <div class="btn-orange read-more" style="left:139px;top:108px">Read more</div>
    </article>
  </section>

  <nav>
    <div class="abs btn-orange browse">Browse Dictionary</div>
    <div class="abs letters">
      <span>A</span><span>B</span><span>C</span><span>D</span><span>E</span><span>F</span><span>G</span><span>H</span><span>I</span><span>J</span><span>K</span><span>E</span><span>L</span><span>M</span><span>N</span><span>O</span><span>P</span><span>Q</span><span>R</span><span>S</span><span>T</span>
    </div>
    <div class="abs next">Next »</div>
  </nav>

  <footer class="abs footer">
    <div class="abs brand"><span class="word">Quill</span><span class="sub">LEXICON</span></div>
    <div class="f-col" style="left:170px"><h4>QuillLexicon.com</h4><ul><li>FAQ</li><li>Contact</li><li>Blog</li></ul></div>
    <div class="f-col" style="left:295px"><h4>Information</h4><ul><li>Legal</li><li>Privacy Policy</li><li>Terms of Use</li></ul></div>
    <div class="f-col" style="left:399px"><h4>Others</h4><ul><li>Popular Words</li><li>Common Errors in English</li><li>Exam Prep Online</li></ul></div>
    <div class="f-col f-news" style="left:528px"><h4>Newsletter</h4><p>Subcribe the news letter signup</p><div class="field">Enter your email address...</div><div class="btn-orange">Subcribe</div></div>
  </footer>

  <div class="abs bottom">
    <span class="abs" style="left:62px;top:12px">Copyright © 2016 Lumenleaf Solutions Pvt. Ltd. All rights reserved.</span>
    <span class="social" style="left:596px;background:#3b5b99"></span>
    <span class="social" style="left:620px;background:#2aa3dd"></span>
    <span class="social" style="left:642px;background:#1a6e9b"></span>
    <span class="social" style="left:664px;background:#d33a2c"></span>
    <span class="abs" style="left:708px;top:12px">C12</span>
  </div>

</div>
</body>
</html>
```